Harbor-Glow

Letter heads, business cards, packaging envelopes big and small, and stationery
We have logo design and trademarked approval, we would lie to
upload design to help create this project.
This product was created for my Mother a 4 time diganosed Cancer
Survivor, This product has patent pending and now will be offered to the general public as well.
We are looking foward to working with all of you as this product
and stationary will be viewed worldwide.
Thanks
The Penwick Family

all ages and worldwide

Business

Must have
• Our Logo

```html
<!DOCTYPE html>
<html lang="en">
<head>
<meta charset="utf-8">
<title>Harbor-Glow Stationery</title>
<link rel="stylesheet" href="https://fonts.googleapis.com/css2?family=Montserrat:wght@700;800&family=Open+Sans:wght@400;600&family=Roboto+Condensed:wght@400&display=swap">
<style>
  :root {
    --backdrop: #7a5338;
    --paper: #ffffff;
    --brand-red: #c1202e;
    --brand-navy: #1d3c73;
    --ink-grey: #4a4a4a;
    --fold-line: #b9b9b9;
    --faint-mark: #ececec;
    --caption: #e8e2dc;
  }
  * { margin: 0; padding: 0; box-sizing: border-box; }
  html, body { width: 734px; height: 1200px; overflow: hidden; }
  body { background: var(--backdrop); position: relative; font-family: "Open Sans", Arial, sans-serif; }

  .envelope {
    position: absolute;
    background: var(--paper);
    box-shadow: 0 2px 8px rgba(0,0,0,.35);
    overflow: hidden;
  }
  .envelope--plain { left: 129px; top: 57px; width: 544px; height: 752px; }
  .envelope--red   { left: 65px;  top: 166px; width: 586px; height: 861px; }
  .envelope--navy  { left: 65px;  top: 278px; width: 586px; height: 749px; }

  .envelope__flap { position: absolute; left: 0; top: 0; width: 100%; display: block; }

  .envelope__brand {
    position: absolute; left: 0; right: 0; text-align: center;
    font-family: "Montserrat", Arial, sans-serif; font-weight: 800;
    font-size: 15px; letter-spacing: .2px;
  }
  .envelope__url {
    position: absolute; left: 0; right: 0; text-align: center;
    font-size: 6px;
  }
  .envelope--plain .envelope__brand { top: 28px; color: var(--brand-red); }
  .envelope--plain .envelope__url   { top: 82px; color: var(--ink-grey); }
  .envelope--red .envelope__brand,
  .envelope--navy .envelope__brand  { top: 36px; color: var(--paper); }
  .envelope--red .envelope__url,
  .envelope--navy .envelope__url    { top: 80px; color: var(--paper); }

  .letterhead {
    position: absolute; left: 44px; top: 388px; width: 586px; height: 754px;
    background: var(--paper);
    box-shadow: 0 3px 10px rgba(0,0,0,.4);
    overflow: hidden;
  }
  .letterhead__header { position: absolute; top: 30px; left: 0; right: 0; text-align: center; }
  .letterhead__brand {
    display: inline-flex; align-items: center; gap: 6px;
    font-family: "Montserrat", Arial, sans-serif; font-weight: 800;
    font-size: 22px; color: var(--brand-red); line-height: 1;
  }
  .letterhead__dot { width: 14px; height: 14px; border-radius: 50%; background: var(--brand-red); }
  .letterhead__tagline {
    font-family: "Montserrat", Arial, sans-serif; font-weight: 700;
    font-size: 9px; color: var(--brand-navy); margin-top: 2px; margin-left: 20px;
  }
  .letterhead__address { font-size: 10px; color: var(--brand-navy); margin-top: 6px; letter-spacing: .3px; }

  .letterhead__mark {
    position: absolute; left: 135px; top: 160px; width: 300px; height: 300px;
    border-radius: 50%; background: var(--faint-mark);
  }

  .letterhead__footer { position: absolute; left: 0; bottom: 0; width: 100%; height: 130px; display: block; }
  .letterhead__url {
    position: absolute; left: 92px; bottom: 20px;
    font-size: 10px; color: var(--paper);
  }

  .caption {
    position: absolute; left: 0; width: 634px; top: 1150px; text-align: center;
    font-family: "Roboto Condensed", Arial, sans-serif; font-size: 15px; color: var(--caption);
  }
</style>
</head>
<body>

  <section class="envelope envelope--plain">
    <svg class="envelope__flap" viewBox="0 0 544 110" height="110">
      <path d="M0 8 Q10 16 30 22 L250 88 Q272 95 294 88 L514 22 Q534 16 544 8" fill="none" stroke="var(--fold-line)" stroke-width="1.2"/>
    </svg>
    <div class="envelope__brand">Harbor-Glow</div>
    <div class="envelope__url">www.harborglow.com</div>
  </section>

  <section class="envelope envelope--red">
    <svg class="envelope__flap" viewBox="0 0 586 104" height="104">
      <path d="M0 0 H586 V12 Q576 26 550 32 L316 96 Q293 104 270 96 L36 32 Q10 26 0 12 Z" fill="var(--brand-red)"/>
    </svg>
    <div class="envelope__brand">Harbor-Glow</div>
    <div class="envelope__url">www.harborglow.com</div>
  </section>

  <section class="envelope envelope--navy">
    <svg class="envelope__flap" viewBox="0 0 586 104" height="104">
      <path d="M0 0 H586 V12 Q576 26 550 32 L316 96 Q293 104 270 96 L36 32 Q10 26 0 12 Z" fill="var(--brand-navy)"/>
    </svg>
    <div class="envelope__brand">Harbor-Glow</div>
    <div class="envelope__url">www.harborglow.com</div>
  </section>

  <article class="letterhead">
    <header class="letterhead__header">
      <div class="letterhead__brand"><span class="letterhead__dot"></span>Harbor-Glow</div>
      <div class="letterhead__tagline">Making the World A Safer Place</div>
      <div class="letterhead__address">Street Name, City, State, zip code</div>
    </header>

    <div class="letterhead__mark"></div>

    <svg class="letterhead__footer" viewBox="0 0 586 130" preserveAspectRatio="none">
      <path d="M0 92 Q200 60 360 74 Q500 86 586 0 V130 H0 Z" fill="var(--brand-red)"/>
      <path d="M0 96 Q200 66 360 80 Q500 92 586 8 V130 H0 Z" fill="var(--paper)"/>
      <path d="M0 100 Q200 72 360 86 Q500 98 586 16 V130 H0 Z" fill="var(--brand-red)"/>
      <path d="M0 104 Q200 78 360 92 Q500 104 586 24 V130 H0 Z" fill="var(--paper)"/>
      <path d="M0 107 Q200 84 360 98 Q500 110 586 30 V130 H0 Z" fill="var(--brand-navy)"/>
    </svg>
    <div class="letterhead__url">www.harborglow.com</div>
  </article>

  <p class="caption">Envelope &nbsp;(13 1/2 X 18 1/2 )</p>

</body>
</html>
```